STI/STD Medical Clinic- Wellspring Crest Partners, Inc Website

We are a STI clinic in florida looking for a website. We want to be professional but also playful. We want a buildout similar to the website listed below as our clinic is very similar to theirs.

This is a great example of a clinic doing similar stuff as us. We obviously do not want their color scheme but their format and buildout work. Please see our logo attached for color schemes etc.

https://bluefernclinicmiami.org

Industry/Entity Type

Medical

Coding

Coded - Design and coding required

Number of Pages Required

5+ page

Font styles to use
Sans Serif

```html
<!DOCTYPE html>
<html lang="en">
<head>
<meta charset="utf-8">
<title>Wellspring Crest Partners – STI Clinic</title>
<link href="https://fonts.googleapis.com/css2?family=Poppins:wght@300;400;500;600;700;800&display=swap" rel="stylesheet">
<style>
:root{
  --blue:#2456e0;
  --navy:#2a3bb8;
  --purple:#7a3fe6;
  --pink:#f64ea6;
  --magenta:#e23fd0;
  --orange:#ff7644;
  --ink:#2b2f3a;
  --muted:#5d6270;
  --sky:#eaf3fd;
  --sky2:#f2f7fe;
  --line:#dfe3ee;
  --grad-btn:linear-gradient(90deg,#f64ea6,#ff7644);
  --grad-head:linear-gradient(90deg,#2456e0,#7a3fe6 50%,#f64ea6);
}
*{box-sizing:border-box;margin:0;padding:0}
html,body{width:1200px;height:4255px;overflow:hidden}
body{position:relative;background:#fff;font-family:"Poppins",sans-serif;color:var(--ink)}
.abs{position:absolute}
.btn{position:absolute;display:flex;align-items:center;justify-content:center;background:var(--grad-btn);color:#fff;border-radius:24px;font-size:14px;font-weight:400;text-transform:uppercase;box-shadow:0 6px 16px rgba(246,78,166,.25);white-space:nowrap}
.grad-text{background:var(--grad-head);-webkit-background-clip:text;background-clip:text;color:transparent}
.section-title{position:absolute;left:0;width:1200px;text-align:center;font-weight:700;font-size:34px;letter-spacing:.5px}
.section-sub{position:absolute;left:0;width:1200px;text-align:center;font-size:12.5px;color:var(--ink);line-height:20px;font-weight:300}

/* header */
.brand{position:absolute;left:58px;top:22px;display:flex;align-items:center;gap:10px}
.brand-dot{width:46px;height:46px;border-radius:50%;background:linear-gradient(135deg,#2456e0,#f64ea6)}
.brand-name{font-weight:700;font-size:20px;color:var(--blue);line-height:22px}
.brand-name small{display:block;font-size:10px;font-weight:500;letter-spacing:2px;color:var(--ink)}
.nav a{position:absolute;top:42px;font-size:12.5px;color:var(--ink);text-decoration:none;white-space:nowrap}
.nav a.active{color:var(--orange)}
.nav a.light{color:#fff}

/* hero */
.hero-title{position:absolute;left:673px;top:212px;font-weight:800;font-size:46px;line-height:49px;letter-spacing:.5px}
.hero-title span{display:block}
.side-icons div{position:absolute;left:1157px;width:36px;height:36px;border-radius:50%;background:#fff;box-shadow:0 3px 10px rgba(0,0,0,.12);display:flex;align-items:center;justify-content:center}

/* service cards */
.card{position:absolute;background:#fff;border:1px solid var(--line);text-align:center}
.card.raised{border:none;box-shadow:0 8px 30px rgba(40,60,120,.12)}
.card .icon{width:72px;height:72px;border-radius:50%;margin:26px auto 0;display:flex;align-items:center;justify-content:center}
.card h3{font-size:17px;font-weight:700;margin-top:14px}
.card p{font-size:11.5px;font-weight:300;line-height:20px;color:var(--muted);margin:8px 24px 0}
.card .more{display:inline-block;margin-top:12px;font-size:11px;font-weight:600;color:var(--orange);text-decoration:underline}

/* about */
.about-copy p{font-size:11.5px;line-height:19.5px;font-weight:300;color:var(--ink);margin-bottom:18px}

/* tabs */
.tabs{position:absolute;left:129px;top:1795px;display:flex;gap:3px}
.tab{width:154px;height:97px;display:flex;flex-direction:column;align-items:center;justify-content:flex-end;padding-bottom:10px;font-size:13px;color:var(--ink);position:relative}
.tab svg{margin-bottom:10px}
.tab.active{background:linear-gradient(135deg,#f64ea6,#ff7644);color:#fff}
.tab.active::after{content:"";position:absolute;bottom:-14px;left:63px;border-left:14px solid transparent;border-right:14px solid transparent;border-top:14px solid #fa5f7a}

/* team */
.member{position:absolute;width:200px;text-align:center}
.member .ring{position:relative;width:182px;height:182px;margin:0 auto}
.member h4{margin-top:34px;font-size:17px;font-weight:700}
.member .role{font-size:14px;font-weight:300;margin-top:2px}
.member .loc{font-size:13px;color:var(--pink);margin-top:18px;font-weight:300}

/* form */
.field{position:absolute;left:592px;width:428px;height:40px;border:1px solid var(--line);border-radius:8px;background:#fff;font-size:11px;color:var(--muted);padding:11px 14px}

/* footer */
.foot-h{position:absolute;top:3960px;font-size:13.5px;font-weight:600;color:var(--pink);letter-spacing:.5px}
.sitemap li{list-style:none;font-size:11.5px;height:22.4px;display:flex;align-items:center;gap:14px;color:var(--ink)}
.sitemap li::before{content:"";width:7px;height:7px;border:2px solid var(--purple);border-radius:50%}
.contact-item{position:absolute;left:889px;display:flex;gap:14px;font-size:11.5px;line-height:17px;color:var(--ink)}
.social span{position:absolute;top:4088px;width:36px;height:36px;border-radius:50%;background:linear-gradient(135deg,#7a3fe6,#f64ea6)}
</style>
</head>
<body>

<!-- HERO BACKGROUND -->
<svg class="abs" style="left:0;top:0" width="1200" height="720" aria-hidden="true">
  <defs>
    <linearGradient id="blobGrad" x1="0" y1="0" x2="1" y2="1">
      <stop offset="0" stop-color="#1fa0f0"/><stop offset=".55" stop-color="#3b5fe6"/><stop offset="1" stop-color="#6a36e0"/>
    </linearGradient>
  </defs>
  <path d="M0 0H1200V560C1100 510 1000 480 900 520C800 560 760 650 620 660C480 670 400 610 250 630C140 645 60 680 0 660Z" fill="#eaf3fd"/>
  <path d="M0 660C80 690 140 650 250 640C400 625 480 690 620 685C760 680 820 600 920 555C1020 510 1110 530 1200 575V720H0Z" fill="#fff"/>
  <path d="M835 0C845 120 930 190 1040 195C1120 198 1170 190 1200 175V0Z" fill="url(#blobGrad)"/>
  <path d="M0 190C30 200 50 260 30 290C15 310 5 300 0 300Z" fill="#f7d3ec" opacity=".7"/>
</svg>

<!-- HEADER -->
<div class="brand">
  <div class="brand-dot"></div>
  <div class="brand-name">Wellspring Crest<small>PARTNERS</small></div>
</div>
<svg class="abs" style="left:412px;top:0" width="2" height="34"><line x1="1" y1="0" x2="1" y2="34" stroke="#ff7644" stroke-width="1.5"/></svg>
<nav class="nav">
  <a class="active" style="left:396px">Home</a>
  <a style="left:452px">About</a>
  <a style="left:505px">Meet The Team</a>
  <a style="left:617px">Services</a>
  <a style="left:686px">News</a>
  <a style="left:737px">Faqs</a>
  <a style="left:784px">Contact</a>
  <a class="light" style="left:852px">Patient Portal</a>
</nav>
<div class="btn" style="left:949px;top:33px;width:190px;height:40px;font-size:13.5px">Book Appointment</div>

<!-- HERO -->
<svg class="abs" style="left:70px;top:160px" width="570" height="430" role="img" aria-label="Photo of a clinician holding a test swab during a consultation">
  <defs>
    <linearGradient id="heroPhoto" x1="0" y1="0" x2="1" y2="1">
      <stop offset="0" stop-color="#e9e3dc"/><stop offset=".5" stop-color="#c9b8a6"/><stop offset="1" stop-color="#4a4f5a"/>
    </linearGradient>
  </defs>
  <path d="M70 60C150 -10 300 10 400 25C500 40 570 80 565 200C560 320 500 400 400 405C300 410 260 355 160 360C60 365 0 330 5 230C10 140 20 100 70 60Z" fill="none" stroke="#3b8df0" stroke-width="5"/>
  <path d="M80 70C155 5 300 25 395 40C490 55 550 90 548 200C545 310 490 385 400 390C300 395 260 340 160 345C70 350 15 320 18 230C20 145 35 110 80 70Z" fill="url(#heroPhoto)"/>
</svg>
<div class="abs" style="left:249px;top:472px;width:140px;height:140px;border-radius:50%;background:#fff;border:4px solid #6a36e0;text-align:center">
  <svg style="margin-top:26px" width="48" height="44" viewBox="0 0 48 44" aria-hidden="true">
    <circle cx="28" cy="20" r="16" fill="none" stroke="#2b2f3a" stroke-width="2"/>
    <text x="28" y="25" text-anchor="middle" font-family="Poppins,sans-serif" font-size="13" font-weight="600" fill="#2b2f3a">24</text>
    <path d="M4 14c0 12 10 24 22 26l4-6-6-4-3 3c-4-2-8-6-10-10l3-3-4-6z" fill="#f64ea6"/>
  </svg>
  <div style="font-weight:700;font-size:16px;margin-top:2px">123.456.7890</div>
</div>

<h1 class="hero-title">
  <span style="color:#2456e0">STI CLINIC</span>
  <span style="color:#2a3bb8">CONFIDENTIAL</span>
  <span style="color:#e23fd0">SERVICES &amp;</span>
  <span style="color:#ff7644">SUPPORTS</span>
</h1>
<p class="abs" style="left:676px;top:421px;font-size:15px;font-weight:400">The Florida Independent Sexual Health Service Clinic</p>
<div class="btn" style="left:679px;top:458px;width:192px;height:40px">Book Appointment</div>

<div class="side-icons">
  <div style="top:291px"><svg width="22" height="22" viewBox="0 0 24 24"><circle cx="12" cy="12" r="11" fill="#2456e0"/><path d="M8 6c0 6 4 10 10 11l1-3-3-2-1.5 1.5c-2-1-3.5-2.5-4.5-4.5L11.5 7.5 9.5 5z" fill="#fff"/></svg></div>
  <div style="top:341px"><svg width="22" height="22" viewBox="0 0 24 24"><circle cx="12" cy="12" r="11" fill="#a045e0"/><rect x="6" y="8" width="12" height="8" rx="1" fill="none" stroke="#fff" stroke-width="1.5"/><path d="M6 8l6 5 6-5" fill="none" stroke="#fff" stroke-width="1.5"/></svg></div>
  <div style="top:389px"><svg width="22" height="22" viewBox="0 0 24 24"><circle cx="12" cy="12" r="11" fill="#f64ea6"/><rect x="7" y="7" width="10" height="10" rx="1" fill="none" stroke="#fff" stroke-width="1.5"/><line x1="7" y1="10" x2="17" y2="10" stroke="#fff" stroke-width="1.5"/></svg></div>
</div>

<!-- SERVICE CARDS -->
<div class="card" style="left:174px;top:811px;width:269px;height:233px">
  <div class="icon" style="background:#e3dcfb"><svg width="34" height="38" viewBox="0 0 34 38"><rect x="7" y="3" width="20" height="32" rx="6" fill="#c9bdf5"/><circle cx="17" cy="22" r="6" fill="#6a36e0"/></svg></div>
  <h3><span class="grad-text">PREP</span></h3>
  <p>Lorem Ipsum has been the industry's standard dummy text ever.</p>
  <span class="more">LEARN MORE</span>
</div>
<div class="card raised" style="left:464px;top:785px;width:271px;height:273px">
  <div class="icon" style="background:#fbd9ef"><svg width="40" height="34" viewBox="0 0 40 34"><path d="M4 14C4 5 14 2 24 4C34 6 38 12 34 20C30 28 20 24 14 30C8 34 4 24 4 14Z" fill="#7a3fe6"/><circle cx="14" cy="14" r="3" fill="#f64ea6"/><circle cx="24" cy="12" r="3" fill="#f64ea6"/></svg></div>
  <h3><span class="grad-text">HEPATITIS C</span></h3>
  <p>Lorem Ipsum has been the industry's standard dummy text ever</p>
  <div class="btn" style="position:relative;margin:14px auto 0;width:120px;height:34px;font-size:12.5px">Learn More</div>
</div>
<div class="card" style="left:757px;top:811px;width:271px;height:233px">
  <div class="icon" style="background:#fde0d3"><svg width="20" height="40" viewBox="0 0 20 40"><path d="M5 34V12a5 5 0 0 1 10 0v22z" fill="#ff7644"/><rect x="2" y="33" width="16" height="4" rx="2" fill="#ff7644"/></svg></div>
  <h3><span class="grad-text">STI</span></h3>
  <p>Lorem Ipsum has been the industry's standard dummy text ever</p>
  <span class="more">LEARN MORE</span>
</div>

<!-- ABOUT -->
<svg class="abs" style="left:160px;top:1130px" width="450" height="480" aria-hidden="true">
  <path d="M80 40C180 -10 330 10 400 80C450 130 440 230 410 300" fill="none" stroke="#d9e6fa" stroke-width="1.5"/>
  <path d="M30 360C10 400 40 470 90 470C140 470 150 420 120 390C95 365 50 330 30 360Z" fill="#fbd3ec" opacity=".7"/>
  <circle cx="66" cy="112" r="58" fill="#fff" stroke="#e6ecf8" stroke-width="1"/>
  <circle cx="66" cy="112" r="26" fill="#eef2fb" stroke="#c9d4f0"/>
</svg>
<svg class="abs" style="left:215px;top:1225px" width="345" height="360" role="img" aria-label="Photo of a doctor holding a tablet showing a glowing body scan with gender symbols">
  <defs>
    <linearGradient id="aboutPhoto" x1="0" y1="0" x2="1" y2="1">
      <stop offset="0" stop-color="#5fa8e8"/><stop offset=".6" stop-color="#2e74c9"/><stop offset="1" stop-color="#e9eef6"/>
    </linearGradient>
  </defs>
  <path d="M10 20H320a10 10 0 0 1 10 10V190A150 150 0 0 1 180 340H170A160 160 0 0 1 10 180Z" fill="none" stroke="#dde9fb" stroke-width="6"/>
  <path d="M18 14H310a10 10 0 0 1 10 10V180A140 140 0 0 1 180 325H170A150 150 0 0 1 18 175Z" fill="url(#aboutPhoto)"/>
</svg>

<div class="abs" style="left:668px;top:1185px;font-size:13px">ABOUT</div>
<h2 class="abs grad-text" style="left:666px;top:1203px;font-size:33px;font-weight:700;letter-spacing:.3px;white-space:nowrap">WELLSPRING CREST</h2>
<div class="abs" style="left:668px;top:1248px;font-size:17.5px;color:#f64ea6;font-weight:400">PARTNERS, INC</div>
<div class="abs about-copy" style="left:670px;top:1286px;width:350px">
  <p>Lorem Ipsum has been the industry's standard dummy text ever since the 1500s, when an unknown printer took a galley of type and scrambled it to make a type specim book. It has survived not only five centuries.</p>
  <p>Lorem Ipsum has been the industry's standard dummy text ever since the 1500s, when an unknown printer took a galley of type and scrambled it to make a type specimen book. It has survived not only five centuries, but also the leap into electronic typesetting, remaining essentially unchanged.</p>
</div>
<div class="btn" style="left:672px;top:1497px;width:137px;height:40px">Learn More</div>

<!-- OUR SERVICES -->
<h2 class="section-title" style="top:1663px"><span class="grad-text">OUR SERVICES</span></h2>
<p class="section-sub" style="top:1718px">Lorem Ipsum has been the industry's standard dummy text ever since thes, when<br>an unknown printer took a galley of type and scrambled.</p>

<div class="tabs">
  <div class="tab active"><svg width="34" height="40" viewBox="0 0 34 40"><rect x="7" y="3" width="20" height="34" rx="6" fill="none" stroke="#fff" stroke-width="2.5"/><circle cx="17" cy="22" r="6" fill="#fff"/></svg>PREP</div>
  <div class="tab" style="background:#cfe5fb"><svg width="40" height="40" viewBox="0 0 40 40"><g transform="rotate(-45 20 20)"><rect x="4" y="13" width="32" height="14" rx="7" fill="#fff" stroke="#1b2450" stroke-width="2"/><path d="M20 13h9a7 7 0 0 1 0 14h-9z" fill="#2456e0"/></g></svg>PEP</div>
  <div class="tab" style="background:#ddd3f8"><svg width="44" height="40" viewBox="0 0 44 40"><path d="M4 16C4 6 16 2 28 5C40 8 42 16 37 24C32 32 20 28 13 35C7 40 4 28 4 16Z" fill="#7a3fe6" stroke="#1b2450" stroke-width="2"/><circle cx="30" cy="12" r="5" fill="#f64ea6"/></svg>HEPATITIS C</div>
  <div class="tab" style="background:#e8dcf8"><svg width="30" height="40" viewBox="0 0 30 40"><path d="M15 4c-5 0-7 4-6 8l12 24M15 4c5 0 7 4 6 8L9 36" fill="none" stroke="#7a3fe6" stroke-width="4"/></svg>HIV</div>
  <div class="tab" style="background:#fad6ee"><svg width="20" height="40" viewBox="0 0 20 40"><path d="M5 34V12a5 5 0 0 1 10 0v22z" fill="#e23fd0" stroke="#1b2450" stroke-width="1.5"/><rect x="2" y="33" width="16" height="4" rx="2" fill="#1b2450"/></svg>STI</div>
  <div class="tab" style="background:#fde0d3"><svg width="34" height="40" viewBox="0 0 34 40"><rect x="6" y="4" width="22" height="30" rx="2" fill="#ff7644" stroke="#1b2450" stroke-width="2"/><line x1="11" y1="12" x2="23" y2="12" stroke="#fff" stroke-width="2"/><line x1="11" y1="18" x2="23" y2="18" stroke="#fff" stroke-width="2"/><line x1="11" y1="24" x2="19" y2="24" stroke="#fff" stroke-width="2"/></svg>CASE MANAGEMENT</div>
</div>

<h3 class="abs grad-text" style="left:183px;top:1988px;font-size:32px;font-weight:700">PREP</h3>
<div class="abs" style="left:184px;top:2040px;width:320px;font-size:11.5px;line-height:20px">
  <p style="margin-bottom:14px">Lorem Ipsum has been the industry's standard dummy text ever since thes, when an unknown printer took a galley of type and scrambled.</p>
  <p style="font-weight:300;color:var(--muted)">but also the leap into electronic typesetting, remaining essentially unchanged. It was popularised in the 1960s with the release of Letraset sheets containing Lorem Ipsum passages, and more recently publis.</p>
</div>
<div class="btn" style="left:184px;top:2210px;width:137px;height:40px">Learn More</div>

<svg class="abs" style="left:605px;top:1970px" width="445" height="350" role="img" aria-label="Photo of a nurse taking a patient's blood sample, with an inset of blue medication capsules">
  <defs>
    <linearGradient id="prepPhoto" x1="0" y1="0" x2="1" y2="1">
      <stop offset="0" stop-color="#dfe6ee"/><stop offset=".5" stop-color="#8fa6c4"/><stop offset="1" stop-color="#3c5a8a"/>
    </linearGradient>
  </defs>
  <path d="M10 170C-10 210 20 240 50 230C40 200 30 180 10 170Z" fill="#fbd3ec"/>
  <path d="M380 80C420 70 445 110 430 150C410 140 390 110 380 80Z" fill="#ffe0d3"/>
  <path d="M80 60C120 10 200 40 260 20C320 0 380 20 400 80C420 140 430 220 380 270C330 320 260 300 200 330C140 355 80 330 50 270C20 210 40 110 80 60Z" fill="url(#prepPhoto)"/>
  <circle cx="370" cy="255" r="56" fill="#fff"/>
  <circle cx="370" cy="255" r="50" fill="#7fb0dc"/>
</svg>

<!-- TEAM -->
<svg class="abs" style="left:0;top:2350px" width="1200" height="600" aria-hidden="true">
  <path d="M0 80C150 20 300 30 460 50C640 72 780 100 940 70C1060 48 1140 20 1200 30V600H0Z" fill="#f1f6fd"/>
</svg>
<h2 class="section-title" style="top:2473px"><span class="grad-text">MEET OUR TEAM</span></h2>
<p class="section-sub" style="top:2521px">Lorem Ipsum has been the industry's standard dummy text ever since.</p>

<div class="member" style="left:87px;top:2578px">
  <div class="ring">
    <svg width="182" height="182" viewBox="0 0 182 182" role="img" aria-label="Portrait photo of a team member">
      <circle cx="91" cy="91" r="88" fill="#fff" stroke="#c9cdf0" stroke-width="1.5"/>
      <path d="M91 3A88 88 0 0 0 91 179" fill="none" stroke="#2456e0" stroke-width="14"/>
      <path d="M91 3A88 88 0 0 1 160 38" fill="none" stroke="#7a3fe6" stroke-width="14"/>
      <circle cx="91" cy="91" r="72" fill="#b7c7dc"/>
    </svg>
    <svg class="abs" style="left:140px;top:120px" width="36" height="36" viewBox="0 0 36 36"><circle cx="18" cy="18" r="17" fill="#f8557f"/><path d="M10 18h15M20 12l6 6-6 6" fill="none" stroke="#fff" stroke-width="2.2"/></svg>
  </div>
  <h4><span class="grad-text">MEMBER NAME</span></h4><div class="role">Medical Provider</div><div class="loc">Location : Florida</div>
</div>
<div class="member" style="left:362px;top:2578px">
  <div class="ring">
    <svg width="182" height="182" viewBox="0 0 182 182" role="img" aria-label="Portrait photo of a team member">
      <circle cx="91" cy="91" r="88" fill="#fff" stroke="#c9cdf0" stroke-width="1.5"/>
      <path d="M15 135A88 88 0 0 0 170 130" fill="none" stroke="#3b3fd0" stroke-width="14"/>
      <path d="M120 8A88 88 0 0 1 170 50" fill="none" stroke="#7a3fe6" stroke-width="14"/>
      <circle cx="91" cy="91" r="72" fill="#e5dcd3"/>
    </svg>
    <svg class="abs" style="left:140px;top:120px" width="36" height="36" viewBox="0 0 36 36"><circle cx="18" cy="18" r="17" fill="#f8557f"/><path d="M10 18h15M20 12l6 6-6 6" fill="none" stroke="#fff" stroke-width="2.2"/></svg>
  </div>
  <h4><span class="grad-text">MEMBER NAME</span></h4><div class="role">Medical Provider</div><div class="loc">Location : Florida</div>
</div>
<div class="member" style="left:639px;top:2578px">
  <div class="ring">
    <svg width="182" height="182" viewBox="0 0 182 182" role="img" aria-label="Portrait photo of a team member">
      <circle cx="91" cy="91" r="88" fill="#fff" stroke="#c9cdf0" stroke-width="1.5"/>
      <path d="M91 3A88 88 0 0 0 15 135" fill="none" stroke="#2456e0" stroke-width="14"/>
      <path d="M91 3A88 88 0 0 1 170 60" fill="none" stroke="#7a3fe6" stroke-width="14"/>
      <circle cx="91" cy="91" r="72" fill="#dfe7f1"/>
    </svg>
    <svg class="abs" style="left:140px;top:120px" width="36" height="36" viewBox="0 0 36 36"><circle cx="18" cy="18" r="17" fill="#f8557f"/><path d="M10 18h15M20 12l6 6-6 6" fill="none" stroke="#fff" stroke-width="2.2"/></svg>
  </div>
  <h4><span class="grad-text">MEMBER NAME</span></h4><div class="role">Medical Provider</div><div class="loc">Location : Florida</div>
</div>
<div class="member" style="left:912px;top:2578px">
  <div class="ring">
    <svg width="182" height="182" viewBox="0 0 182 182" role="img" aria-label="Portrait photo of a team member">
      <circle cx="91" cy="91" r="88" fill="#fff" stroke="#c9cdf0" stroke-width="1.5"/>
      <path d="M12 130A88 88 0 0 0 165 140" fill="none" stroke="#3b3fd0" stroke-width="14"/>
      <path d="M150 25A88 88 0 0 1 178 100" fill="none" stroke="#2456e0" stroke-width="14"/>
      <circle cx="91" cy="91" r="72" fill="#d3dbe6"/>
    </svg>
    <svg class="abs" style="left:140px;top:120px" width="36" height="36" viewBox="0 0 36 36"><circle cx="18" cy="18" r="17" fill="#f8557f"/><path d="M10 18h15M20 12l6 6-6 6" fill="none" stroke="#fff" stroke-width="2.2"/></svg>
  </div>
  <h4><span class="grad-text">MEMBER NAME</span></h4><div class="role">Medical Provider</div><div class="loc">Location : Florida</div>
</div>

<!-- BOOK APPOINTMENT -->
<svg class="abs" style="left:0;top:3060px" width="510" height="400" role="img" aria-label="Photo of a doctor speaking with a patient in an exam room">
  <defs>
    <linearGradient id="bookPhoto" x1="0" y1="0" x2="1" y2="1">
      <stop offset="0" stop-color="#eef1f4"/><stop offset=".5" stop-color="#b9c4d2"/><stop offset="1" stop-color="#3a6fb8"/>
    </linearGradient>
  </defs>
  <path d="M0 10H320A180 180 0 0 1 320 390H0Z" fill="none" stroke="#dbe8fb" stroke-width="6"/>
  <path d="M0 22H315A168 168 0 0 1 315 368H0Z" fill="url(#bookPhoto)"/>
</svg>
<svg class="abs" style="left:1060px;top:3180px" width="140" height="330" aria-hidden="true">
  <path d="M140 10C60 40 20 120 40 200C60 270 110 310 140 320" fill="none" stroke="#e3ebf8"/>
  <path d="M140 40C80 70 50 130 65 200C80 260 115 290 140 300" fill="none" stroke="#e3ebf8"/>
  <path d="M140 90C110 110 100 170 120 220C128 240 135 250 140 255Z" fill="#fbd3ec" opacity=".7"/>
</svg>

<h2 class="abs grad-text" style="left:591px;top:3010px;font-size:33px;line-height:38px;font-weight:700;letter-spacing:.5px">BOOK AN<br>APPOINTMENT</h2>
<p class="abs" style="left:593px;top:3097px;font-size:13px;white-space:nowrap">Want to Hear More About Wellspring Crest Partners</p>
<div class="field" style="top:3136px">Name *</div>
<div class="field" style="top:3188px">Email *</div>
<div class="field" style="top:3239px">Phone *</div>
<div class="field" style="top:3290px">Discussion For *</div>
<div class="field" style="top:3341px;height:81px">Message *</div>
<div class="btn" style="left:592px;top:3443px;width:99px;height:40px;border-radius:20px">Submit</div>

<!-- CALLOUT -->
<div class="abs" style="left:563px;top:3560px;width:74px;height:74px;border-radius:50%;border:3px solid #c9d4f0"></div>
<h2 class="section-title" style="top:3660px"><span class="grad-text">HOW DO I KNOW IF I HAVE AN STI ?</span></h2>
<p class="section-sub" style="top:3716px;font-size:14.5px;line-height:23px;font-weight:400">You can have an STI without knowing it. Get tested. It's the only<br>way to be sure.</p>
<div class="btn" style="left:456px;top:3782px;width:136px;height:40px">View Services</div>
<div class="btn" style="left:607px;top:3782px;width:137px;height:40px">Contact Us</div>

<!-- FOOTER -->
<svg class="abs" style="left:0;top:3780px" width="1200" height="475" aria-hidden="true">
  <path d="M0 120C160 60 300 150 460 140C620 130 700 70 860 80C1000 90 1100 140 1200 110V475H0Z" fill="#f1f6fd"/>
  <path d="M0 70C40 80 80 130 90 180C95 210 60 220 30 210C10 205 0 195 0 190Z" fill="#fbd3ec" opacity=".6"/>
  <path d="M1200 370C1150 380 1100 410 1095 475H1200Z" fill="#ffe3d6" opacity=".6"/>
</svg>

<div class="abs" style="left:80px;top:4010px;display:flex;align-items:center;gap:12px">
  <div style="width:60px;height:60px;border-radius:50%;background:linear-gradient(135deg,#2456e0,#f64ea6)"></div>
  <div style="font-weight:700;font-size:24px;line-height:26px;color:var(--blue);white-space:nowrap">Wellspring Crest<small style="display:block;font-size:12px;letter-spacing:3px;color:var(--ink);font-weight:500">PARTNERS</small></div>
</div>
<div class="social" aria-label="Social links">
  <span style="left:108px"></span><span style="left:149px"></span><span style="left:190px"></span><span style="left:231px"></span>
</div>

<div class="foot-h" style="left:362px">SITEMAP</div>
<ul class="abs sitemap" style="left:360px;top:3999px">
  <li>Home</li><li>About</li><li>Meet the team</li><li>Services</li><li>News</li><li>Faq's</li><li>Contact Us</li>
</ul>

<div class="foot-h" style="left:593px">COMMUNITY FEED</div>
<div class="abs" style="left:593px;top:4002px;width:238px;height:164px;background:#fff;box-shadow:0 4px 18px rgba(40,60,120,.08)">
  <div class="abs" style="left:18px;top:20px;width:34px;height:34px;border:1px solid var(--line);border-radius:3px"></div>
  <div class="abs" style="left:62px;top:22px;font-size:9.5px;color:var(--blue);white-space:nowrap">WELLSPRING CREST PARTNERS</div>
  <div class="abs" style="left:62px;top:37px;font-size:8px;color:var(--muted)">134 likes</div>
  <div class="abs" role="img" aria-label="Photo of smiling people gathered together" style="left:18px;top:66px;width:204px;height:50px;background:linear-gradient(90deg,#6b4a3a,#c99b7a 50%,#7a5a4a)"></div>
  <div class="abs" style="left:18px;top:128px;font-size:8px;color:var(--blue)">Share</div>
  <div class="abs" style="left:160px;top:128px;font-size:8px;color:var(--blue)">View feed</div>
</div>

<div class="foot-h" style="left:889px">CONTACT US</div>
<div class="contact-item" style="top:4003px">
  <svg width="20" height="24" viewBox="0 0 20 24"><path d="M10 1a8 8 0 0 0-8 8c0 6 8 14 8 14s8-8 8-14a8 8 0 0 0-8-8z" fill="none" stroke="#e23fd0" stroke-width="1.6"/><circle cx="10" cy="9" r="3" fill="none" stroke="#e23fd0" stroke-width="1.6"/></svg>
  <div>WELLSPRING CREST<br>florida - Address city state conutry</div>
</div>
<div class="contact-item" style="top:4053px">
  <svg width="20" height="20" viewBox="0 0 20 20"><path d="M4 2c0 8 6 14 14 15l1-4-4-2-2 2c-3-1-5-3-6-6l2-2-2-4z" fill="none" stroke="#e23fd0" stroke-width="1.6"/></svg>
  <div>Call Us: 123.456.7890</div>
</div>
<div class="contact-item" style="top:4088px">
  <svg width="20" height="20" viewBox="0 0 20 20"><rect x="5" y="2" width="10" height="5" fill="none" stroke="#e23fd0" stroke-width="1.6"/><rect x="2" y="7" width="16" height="8" rx="1" fill="none" stroke="#e23fd0" stroke-width="1.6"/><rect x="5" y="12" width="10" height="6" fill="#fff" stroke="#e23fd0" stroke-width="1.6"/></svg>
  <div>Fax Us: 123.456.7890</div>
</div>
<div class="contact-item" style="top:4124px">
  <svg width="20" height="20" viewBox="0 0 20 20"><rect x="2" y="4" width="16" height="12" rx="1" fill="none" stroke="#e23fd0" stroke-width="1.6"/><path d="M2 4l8 7 8-7" fill="none" stroke="#e23fd0" stroke-width="1.6"/></svg>
  <div>info@wellspringcrest.com</div>
</div>

<p class="abs" style="left:0;top:4227px;width:1200px;text-align:center;font-size:11px;color:var(--ink)"><span style="color:var(--pink)">©WELLSPRING CREST PARTNERS</span> - 2022 All rights reserved</p>

</body>
</html>
```